Dive Bar/ Pop Culture Bar Adult Nugget Night

Hey guys,
Lorne here from Rusty Gabs restaurant in Australia. Im after a poster design for our new Monday Night Special - Adult Nugget Night. - Think crumbed chicken or Beef Schnitzel with different toppings like Philly Cheese steak or Cheese burger smash (aka a parmy).

I'm thinking a plain block blue colour background with a vector image as the main focus - see attached graphics. I would like the poster to be a fun and tongue in cheek and a 80's/90's hip hop vibe and vector image of a nugget "thug life".

The info it has to contain are as follows -
- Adult Nugget Night (title)
- Monday Night
- Price $17
- from 5pm

Toppings
- Philly Cheese Steak
- Cheese burger Smash
- Burnt End Beanz

A little about Rusty Gabs
-Rusty Gabs came about because we fell in love with the old- skool American south culture of slow cooked soul food, thrown together on big hearty share plates in the backyard and tucked into with the ones you love.

We wanted to bring something different to the coast.

Moody and grungy without losing the soul of why we go out to drink and eat in the first place - to fill our bellies and warm our hearts.

That's why communal eating is at the core of what we do. Low 'n' Slow platters of scrumptious, fall off the bone meat. Sided with delicious dishes of your choice. That quietness that falls on the table as everyone savours the flavours. Laughs as you reach across your mate, to fork that last juicy piece of slow cooked meat that someone else was eyeing off. Washing it all down with hand-crafted beer, or better yet, that top shelf whiskey glistening from the back bar. Finishing off the night with the best kind of dessert.. our famous Sticky Date Espresso Martini!

I have found one image on the net that I like....... don't know if it's useful...

Please reach out for any more info or questions needed

Cheers
Lorne

Target Market(s)

20-40 year old for a funky grudge bar

Industry/Entity Type

Dive Bar, Smokehouse, Bar & Grill

Font styles to use
Other font styles liked:
• Veneer

Colors
0054AA
0677BA
7BADD7
CADEEF
E8F1F8
FFF300
FFF600
FEFA6F
FFFEC7
FFFEE8
F0912C
F2A743
F7CA91
FBE8D2
FDF5EE
EB3D1F
EC4F4E
F09395
F8D3D4
FCEDEE

Requirements
Must have
• Business Name "Rusty Gabs" will share Logo in later stages
Nice to have
• Nice bold colours which throw back to 1980/90's pop culture

```html
<!DOCTYPE html>
<html lang="en">
<head>
<meta charset="utf-8">
<title>Adult Nugget Night – Rusty Gabs</title>
<link rel="stylesheet" href="https://fonts.googleapis.com/css2?family=Alfa+Slab+One&family=Anton&family=Archivo:ital,wght@0,400;1,800&family=Roboto+Condensed:wght@400&family=Lexend:wght@600&display=swap">
<style>
  :root {
    --bg: #5733db;
    --bg-deep: #4524c4;
    --panel: #3a17a8;
    --price-box: #4b2ab6;
    --band: rgba(70, 55, 110, 0.85);
    --plaque: #3828c6;
    --ink: #0b0626;
    --white: #ffffff;
    --pink: #f3a6f0;
    --brand: #7a4fe0;
    --yellow: #ffe600;
    --nugget: #e4651d;
    --nugget-dark: #b2400e;
  }
  * { box-sizing: border-box; margin: 0; padding: 0; }
  html, body { width: 848px; height: 1200px; overflow: hidden; background: var(--bg); }
  .poster {
    position: relative;
    width: 848px;
    height: 1200px;
    overflow: hidden;
    background:
      radial-gradient(ellipse 60% 40% at 25% 20%, rgba(140, 110, 255, 0.45), transparent 70%),
      radial-gradient(ellipse 70% 30% at 80% 70%, rgba(150, 120, 230, 0.35), transparent 70%),
      linear-gradient(180deg, var(--bg) 0%, var(--bg-deep) 100%);
    font-family: "Roboto Condensed", sans-serif;
    color: var(--white);
  }
  .stage-arc {
    position: absolute;
    left: -120px;
    top: -60px;
    width: 1300px;
    height: 1120px;
  }
  .brand {
    position: absolute;
    left: 58px;
    top: 100px;
    font-family: "Lexend", sans-serif;
    font-weight: 600;
    font-size: 20px;
    line-height: 1;
    color: var(--brand);
    white-space: nowrap;
  }
  .price {
    position: absolute;
    left: 640px;
    top: 0;
    width: 146px;
    height: 247px;
    background: var(--price-box);
    text-align: center;
    padding-top: 62px;
  }
  .price__label {
    font-family: "Archivo", sans-serif;
    font-weight: 800;
    font-style: italic;
    font-size: 31px;
    line-height: 1;
    letter-spacing: 1px;
  }
  .price__amount {
    font-family: "Anton", sans-serif;
    font-size: 92px;
    line-height: 1;
    color: var(--yellow);
    margin-top: 6px;
  }
  .mascot {
    position: absolute;
    left: 264px;
    top: 22px;
    width: 332px;
    height: 420px;
    border-radius: 48% 48% 42% 42% / 40% 40% 55% 55%;
    background: radial-gradient(ellipse at 55% 60%, var(--nugget) 0%, var(--nugget-dark) 90%);
    border: 4px solid var(--ink);
    box-shadow: 0 0 0 4px var(--white);
  }
  .title {
    position: absolute;
    left: 167px;
    top: 428px;
    width: 531px;
    height: 282px;
    background: var(--plaque);
    border: 5px solid var(--ink);
    border-radius: 36px;
    box-shadow: 0 0 0 4px rgba(211, 92, 255, 0.6), 0 0 24px 8px rgba(211, 92, 255, 0.55);
    text-align: center;
    font-family: "Alfa Slab One", serif;
    color: var(--white);
    -webkit-text-stroke: 1.5px var(--pink);
  }
  .title__top {
    display: block;
    font-size: 64px;
    line-height: 1;
    margin-top: 22px;
    white-space: nowrap;
  }
  .title__bottom {
    display: block;
    font-size: 140px;
    line-height: 1;
    letter-spacing: 12px;
    margin-left: 12px;
    margin-top: 0;
  }
  .when {
    position: absolute;
    left: 0;
    top: 721px;
    width: 848px;
    height: 53px;
    background: var(--band);
    text-align: center;
    font-size: 42px;
    line-height: 53px;
    letter-spacing: 2px;
  }
  .toppings {
    position: absolute;
    left: 24px;
    top: 784px;
    width: 815px;
    display: flex;
    gap: 15px;
  }
  .topping {
    flex: 1;
    height: 133px;
    background: var(--panel);
    border-radius: 20px;
    padding: 14px 10px 0 14px;
  }
  .topping__name {
    font-family: "Lexend", sans-serif;
    font-weight: 600;
    font-size: 20px;
    letter-spacing: 1.2px;
    white-space: nowrap;
    text-align: center;
    line-height: 1.1;
  }
  .topping__desc {
    width: 236px;
    font-size: 12.2px;
    line-height: 17px;
    margin-top: 14px;
    letter-spacing: 0.5px;
  }
  .about__heading {
    position: absolute;
    left: 14px;
    top: 925px;
    width: 370px;
    height: 50px;
    background: var(--ink);
    box-shadow: 3px 4px 0 var(--white);
    font-family: "Anton", sans-serif;
    font-size: 27px;
    font-weight: 400;
    letter-spacing: 2.4px;
    line-height: 50px;
    padding-left: 26px;
    z-index: 2;
  }
  .about {
    position: absolute;
    left: 14px;
    top: 967px;
    width: 818px;
    height: 219px;
    background: var(--panel);
    padding: 24px 20px 0 23px;
    font-family: "Archivo", sans-serif;
    font-weight: 800;
    font-style: italic;
    font-size: 11.6px;
    line-height: 18.5px;
    letter-spacing: 0.9px;
  }
  .about p.indent { text-indent: 22px; }
</style>
</head>
<body>
<main class="poster">
  <svg class="stage-arc" viewBox="0 0 1300 1120" aria-hidden="true">
    <path d="M60 0 C 220 600, 700 980, 1300 1020 L1300 1120 C 640 1080, 160 680, 0 20 Z" fill="rgba(180,160,255,0.28)"/>
  </svg>

  <div class="brand">Rusty Gabs</div>

  <aside class="price">
    <div class="price__label">Price<br>Start</div>
    <div class="price__amount">$17</div>
  </aside>

  <div class="mascot" role="img" aria-label="Mascot illustration: a cartoon crumbed chicken nugget character"></div>

  <h1 class="title">
    <span class="title__top">Adult Nugget</span>
    <span class="title__bottom">Night</span>
  </h1>

  <div class="when">Monday Night &nbsp;- &nbsp;from 5pm</div>

  <section class="toppings">
    <article class="topping">
      <h2 class="topping__name">Philly Cheese Steak</h2>
      <p class="topping__desc">Think crumbed chicken or Beef Schnitzel with different toppings like Philly Cheese steak or Cheese burger smash (aka parmy).</p>
    </article>
    <article class="topping">
      <h2 class="topping__name">Cheese burger Smash</h2>
      <p class="topping__desc">Think crumbed chicken or Beef Schnitzel with different toppings like Philly Cheese steak or Cheese burger smash (aka parmy).</p>
    </article>
    <article class="topping">
      <h2 class="topping__name">Burnt End Beanz</h2>
      <p class="topping__desc">Think crumbed chicken or Beef Schnitzel with different toppings like Philly Cheese steak or Cheese burger smash (aka parmy).</p>
    </article>
  </section>

  <h2 class="about__heading">A LITTLE ABOUT RUSTY GABS</h2>
  <section class="about">
    <p>Rusty Gabs came about because we fell in love with the old- skool American south culture of slow cooked soul food, thrown together on big hearty share plates in the backyard and tucked into with the ones you love.</p>
    <p class="indent">We wanted to bring something different to the coast.Moody and grungy without losing the soul of why we go out to drink and eat in the first place - to fill our bellies and warm our hearts.</p>
    <p>That's why communal eating is at the core of what we do. Low 'n' Slow platters of scrumptious, fall off the bone meat. Sided with delicious dishes of your choice. That quietness that falls on the table as everyone savours the flavours. Laughs as you reach across your mate, to fork that last juicy piece of slow cooked meat that someone else was eyeing off. Washing it all down with hand-crafted beer, or better yet, that top shelf whiskey glistening from the back bar. Finishing off the night with the best kind of dessert.. our famous Sticky Date Espresso Martini!</p>
  </section>
</main>
</body>
</html>
```